Criação de Papelaria Profissional para Educação & Cursos
" A empresa é nova. Vamos ensinar projetistas a utilizar a plataforma BIM-Kolmar. Com esse curso os profissionais ganharão em produtividade e qualidade. "

```html
<!DOCTYPE html>
<html lang="pt-BR">
<head>
<meta charset="utf-8">
<title>zanbiq — Cartões de visita</title>
<link rel="stylesheet" href="https://fonts.googleapis.com/css2?family=Montserrat:wght@400;500;700&display=swap">
<style>
  :root {
    --yellow: #f8c93c;
    --yellow-deep: #f2b705;
    --ink: #1f1f1f;
    --card-black: #1b1b1b;
    --white: #ffffff;
    --muted: #4a4a4a;
  }
  * { box-sizing: border-box; margin: 0; padding: 0; }
  html, body { width: 1200px; height: 1200px; overflow: hidden; }
  body {
    background: var(--yellow);
    font-family: "Montserrat", sans-serif;
    color: var(--ink);
    position: relative;
  }
  .card {
    position: absolute;
    left: 165px;
    width: 870px;
    height: 483px;
    border-radius: 26px;
    overflow: hidden;
  }
  .card--front {
    top: 70px;
    background: var(--white);
    border-bottom: 9px solid var(--yellow-deep);
  }
  .card--back {
    top: 637px;
    background: var(--card-black);
    border-bottom: 9px solid var(--yellow-deep);
  }
  .card__texture { position: absolute; inset: 0; }
  .card--front .card__texture { background: linear-gradient(135deg, #ffffff, #f4f4f4); }
  .card--back .card__texture { background: linear-gradient(135deg, #222222, #161616); }

  .brand {
    position: absolute;
    display: flex;
    align-items: center;
    gap: 16px;
    font-weight: 700;
    letter-spacing: 1px;
    white-space: nowrap;
  }
  .brand__dot {
    width: 30px; height: 30px;
    border-radius: 50%;
    background: var(--yellow-deep);
  }
  .card--front .brand { left: 70px; top: 200px; font-size: 62px; color: var(--ink); }
  .card--back .brand {
    left: 50%; top: 50%;
    transform: translate(-50%, -50%);
    font-size: 96px; color: var(--white);
  }
  .card--back .brand__dot { width: 44px; height: 44px; }

  .contact { position: absolute; left: 470px; top: 118px; }
  .contact__person {
    border-left: 6px solid var(--yellow-deep);
    padding-left: 14px;
    margin-bottom: 30px;
  }
  .contact__name { font-weight: 700; font-size: 27px; letter-spacing: 0.5px; }
  .contact__role { font-size: 20px; color: var(--muted); margin-top: 2px; }
  .contact__list { list-style: none; }
  .contact__item {
    display: flex; align-items: center; gap: 14px;
    font-size: 19px; color: var(--muted);
    margin-bottom: 14px; line-height: 1.15;
  }
  .contact__icon {
    flex: none;
    width: 30px; height: 30px; border-radius: 50%;
    background: var(--yellow-deep);
    display: flex; align-items: center; justify-content: center;
  }
  .contact__icon svg { width: 16px; height: 16px; fill: none; stroke: var(--white); stroke-width: 2.2; stroke-linecap: round; stroke-linejoin: round; }
  .contact__item--address { align-items: flex-start; }

  .back__bar {
    position: absolute;
    left: 50%; bottom: 14px;
    transform: translateX(-50%);
    width: 380px; height: 10px;
    border-radius: 5px;
    background: var(--yellow-deep);
  }
</style>
</head>
<body>
  <section class="card card--front" aria-label="Frente do cartão">
    <div class="card__texture" role="img" aria-label="Padrão suave de figuras em cinza claro no fundo branco"></div>
    <div class="brand"><span class="brand__dot"></span>zanbiq</div>
    <div class="contact">
      <div class="contact__person">
        <p class="contact__name">NOME E SOBRENOME</p>
        <p class="contact__role">Cargo | Função</p>
      </div>
      <ul class="contact__list">
        <li class="contact__item">
          <span class="contact__icon"><svg viewBox="0 0 24 24"><path d="M5 4h4l2 5-3 2a11 11 0 0 0 5 5l2-3 5 2v4a2 2 0 0 1-2 2A16 16 0 0 1 3 6a2 2 0 0 1 2-2z"/></svg></span>
          (00) 0000-0000
        </li>
        <li class="contact__item">
          <span class="contact__icon"><svg viewBox="0 0 24 24"><rect x="3" y="6" width="18" height="12" rx="2"/><path d="M3 7l9 6 9-6"/></svg></span>
          contato@exemplo.com
        </li>
        <li class="contact__item">
          <span class="contact__icon"><svg viewBox="0 0 24 24"><circle cx="12" cy="12" r="9"/><path d="M3 12h18M12 3c3 3 3 15 0 18M12 3c-3 3-3 15 0 18"/></svg></span>
          www.exemplo.com.br
        </li>
        <li class="contact__item contact__item--address">
          <span class="contact__icon"><svg viewBox="0 0 24 24"><path d="M12 21s-7-7-7-12a7 7 0 0 1 14 0c0 5-7 12-7 12z"/><circle cx="12" cy="9" r="2.5"/></svg></span>
          <span>rua exemplo, sl 000<br>cidade-UF, CEP: 00000-000</span>
        </li>
      </ul>
    </div>
  </section>

  <section class="card card--back" aria-label="Verso do cartão">
    <div class="card__texture" role="img" aria-label="Padrão suave de figuras em cinza escuro no fundo preto"></div>
    <div class="brand"><span class="brand__dot"></span>zanbiq</div>
    <div class="back__bar"></div>
  </section>
</body>
</html>
```